Larkspur Ridge Management - Business Cards

I need business cards. My current logo was designed by a designer at this site and I very much like and am happy with the results. I would like a business card that is trendy, unique, current yet professional. I deal with high net worth clients daily

Target Market(s)

Out of state investors looking to get into the rental market in Ohio

Industry/Entity Type

Property Management, Consulting

Contact Information for Business Card

Name, Title (Chief Financial Officer) office phone number (555) 817-3094 website address larkridgemgmt.example

Font styles to use
Sans Serif

Colors
0054AA
0677BA
7BADD7
CADEEF
E8F1F8
0094D4
00A9DD
6FCCEA
C7EBF8
E9F6FB
00AB8E
00BBA5
67D7C9
C6EFE9
E9F9F6

```html
<!DOCTYPE html>
<html lang="en">
<head>
<meta charset="utf-8">
<title>Larkspur Ridge Management – Business Cards</title>
<link rel="stylesheet" href="https://fonts.googleapis.com/css2?family=Open+Sans:wght@400;600;700&display=swap">
<style>
  :root {
    --backdrop: #2c2d2f;
    --card: #ffffff;
    --navy: #1f3766;
    --red: #c8202f;
    --ink: #4a4d52;
    --rule: #d9434f;
  }
  * { box-sizing: border-box; margin: 0; padding: 0; }
  html, body {
    width: 1200px;
    height: 900px;
    overflow: hidden;
    background: var(--backdrop);
    font-family: "Open Sans", Arial, sans-serif;
  }
  .stage {
    position: relative;
    width: 1200px;
    height: 900px;
  }
  .card {
    position: absolute;
    left: 285px;
    width: 630px;
    height: 360px;
    background: var(--card);
    box-shadow: 0 14px 30px rgba(0,0,0,.45);
  }
  .card--front { top: 50px; }
  .card--back  { top: 470px; }

  .brand-name {
    font-weight: 700;
    color: var(--navy);
    text-transform: uppercase;
    letter-spacing: .04em;
    line-height: 1.15;
    display: flex;
    align-items: center;
    gap: 12px;
  }
  .brand-mark {
    flex: none;
    width: 16px;
    height: 16px;
    background: var(--navy);
  }
  .card--front .brand-name {
    position: absolute;
    left: 0; right: 0;
    top: 150px;
    justify-content: center;
    font-size: 26px;
  }
  .card--back .brand-name {
    position: absolute;
    right: 40px;
    top: 60px;
    font-size: 17px;
    text-align: right;
    max-width: 260px;
  }
  .card--back .brand-mark { width: 12px; height: 12px; }

  .holder {
    position: absolute;
    left: 40px;
    top: 205px;
    right: 40px;
  }
  .holder-name {
    font-size: 17px;
    font-weight: 600;
    color: var(--navy);
    text-transform: uppercase;
    letter-spacing: .01em;
  }
  .holder-role {
    display: flex;
    align-items: center;
    gap: 8px;
    font-size: 16px;
    color: var(--red);
  }
  .holder-role::after {
    content: "";
    flex: 1;
    height: 1px;
    background: var(--rule);
  }
  .contact {
    list-style: none;
    margin-top: 14px;
    margin-left: 30px;
    font-size: 15px;
    color: var(--ink);
  }
  .contact li {
    display: flex;
    align-items: center;
    gap: 10px;
    height: 27px;
  }
  .contact svg { width: 15px; height: 15px; flex: none; }
</style>
</head>
<body>
<main class="stage">
  <section class="card card--front" aria-label="Card front">
    <div class="brand-name"><span class="brand-mark"></span>Larkspur Ridge Management</div>
  </section>

  <section class="card card--back" aria-label="Card back">
    <div class="brand-name"><span class="brand-mark"></span>Larkspur Ridge Management</div>
    <div class="holder">
      <p class="holder-name">Avery Lindqvist</p>
      <p class="holder-role">Chief Financial Officer</p>
      <ul class="contact">
        <li>
          <svg viewBox="0 0 24 24" aria-hidden="true"><path fill="#1f3766" d="M6.6 10.8a15.2 15.2 0 0 0 6.6 6.6l2.2-2.2a1 1 0 0 1 1-.25 11.4 11.4 0 0 0 3.6.57 1 1 0 0 1 1 1V20a1 1 0 0 1-1 1A17 17 0 0 1 3 4a1 1 0 0 1 1-1h3.5a1 1 0 0 1 1 1c0 1.25.2 2.45.57 3.57a1 1 0 0 1-.25 1z"/></svg>
          (555) 817-3094
        </li>
        <li>
          <svg viewBox="0 0 24 24" aria-hidden="true" fill="none" stroke="#1f3766" stroke-width="1.6"><circle cx="12" cy="12" r="9.5"/><ellipse cx="12" cy="12" rx="4" ry="9.5"/><path d="M2.5 12h19M4 7h16M4 17h16"/></svg>
          larkridgemgmt.example
        </li>
      </ul>
    </div>
  </section>
</main>
</body>
</html>
```